Business Card *

A business card design
Use the logo uploaded in the brief page.
You may use placeholders in your design layouts.
I will provide the actual business card details to the winning designer.

Logo
Place for contact info (name, title, phone, email, etc)

Requirements
Must have
• Logo

```html
<!DOCTYPE html>
<html lang="en">
<head>
<meta charset="utf-8">
<title>Harrowfield — Business Card</title>
<link rel="stylesheet" href="https://fonts.googleapis.com/css2?family=Source+Sans+3:wght@400;600;700;800&display=swap">
<style>
  :root {
    --page-bg: #e6e6e6;
    --brand-green: #3aae49;
    --leaf-green: #8cc63f;
    --card-white: #f4f4f4;
    --ink-grey: #5a5a5a;
    --mark-grey: #8a8a8a;
    --white: #ffffff;
  }
  * { margin: 0; padding: 0; box-sizing: border-box; }
  html, body {
    width: 1200px; height: 960px; overflow: hidden;
    background: var(--page-bg);
    font-family: "Source Sans 3", sans-serif;
  }
  .stage { position: relative; width: 1200px; height: 960px; }
  .card {
    position: absolute; left: 305px; width: 590px; height: 336px; overflow: hidden;
  }
  .card--front { top: 132px; background: var(--brand-green); }
  .card--back { top: 521px; background: var(--card-white); }

  .front-disc {
    position: absolute; left: -90px; top: 20px; width: 350px; height: 350px;
    border-radius: 50%; border: 18px solid var(--white);
  }
  .front-wordmark {
    position: absolute; right: 48px; top: 254px;
    color: var(--white); font-weight: 800; font-size: 31px; letter-spacing: 0.5px;
  }

  .back-disc {
    position: absolute; left: 330px; top: 20px; width: 280px; height: 280px;
    border-radius: 50%; border: 16px solid #e9ece8;
  }
  .back-logo {
    position: absolute; left: 38px; top: 40px; width: 220px;
    display: flex; align-items: center; gap: 10px;
  }
  .back-logo__dot {
    width: 26px; height: 26px; border-radius: 50%; background: var(--brand-green); flex: none;
  }
  .back-wordmark {
    color: var(--mark-grey); font-weight: 800; font-size: 29px; letter-spacing: 0.3px;
  }

  .person { position: absolute; left: 38px; top: 202px; }
  .person__name { color: var(--brand-green); font-weight: 600; font-size: 20px; line-height: 1.1; }
  .person__title { color: var(--ink-grey); font-size: 15px; margin-top: 6px; }

  .contact {
    position: absolute; left: 320px; top: 206px;
    color: var(--ink-grey); font-size: 15px; line-height: 20px;
  }
  .contact__row { display: flex; align-items: center; gap: 6px; }
  .contact__lines { margin-bottom: 8px; }
  .contact__icon { width: 13px; height: 13px; flex: none; }

  .wave { position: absolute; left: 0; bottom: 0; width: 590px; height: 70px; }
  .website {
    position: absolute; left: 40px; bottom: 13px;
    color: var(--white); font-size: 15px;
  }
</style>
</head>
<body>
<main class="stage">

  <section class="card card--front" aria-label="Card front">
    <div class="front-disc"></div>
    <div class="front-wordmark">HARROWFIELD</div>
  </section>

  <section class="card card--back" aria-label="Card back">
    <div class="back-disc"></div>

    <div class="back-logo">
      <span class="back-logo__dot"></span>
      <span class="back-wordmark">HARROWFIELD</span>
    </div>

    <div class="person">
      <div class="person__name">Daniel Reyes</div>
      <div class="person__title">Founder</div>
    </div>

    <div class="contact">
      <div class="contact__lines">
        <div>240 Meadow Lane, Suite 410</div>
        <div>Cedar Falls, Iowa, 50613</div>
      </div>
      <div class="contact__row">
        <svg class="contact__icon" viewBox="0 0 24 24"><path fill="#3aae49" d="M6.6 10.8c1.4 2.8 3.8 5.1 6.6 6.6l2.2-2.2c.3-.3.7-.4 1-.2 1.1.4 2.3.6 3.6.6.6 0 1 .4 1 1V20c0 .6-.4 1-1 1C10.6 21 3 13.4 3 4c0-.6.4-1 1-1h3.5c.6 0 1 .4 1 1 0 1.3.2 2.5.6 3.6.1.3 0 .7-.2 1l-2.3 2.2z"/></svg>
        <span>(555) 010-2040</span>
      </div>
      <div class="contact__row">
        <svg class="contact__icon" viewBox="0 0 24 24"><rect x="2" y="5" width="20" height="14" fill="none" stroke="#3aae49" stroke-width="2.5"/><path d="M2 5l10 8 10-8" fill="none" stroke="#3aae49" stroke-width="2.5"/></svg>
        <span>daniel@harrowfieldagri.com</span>
      </div>
    </div>

    <svg class="wave" viewBox="0 0 590 70" preserveAspectRatio="none">
      <path d="M0 8 C140 -4 300 20 420 30 C500 36 560 26 590 16 L590 70 L0 70 Z" fill="#8cc63f"/>
      <path d="M0 22 C150 12 300 40 430 46 C510 49 560 38 590 30 L590 70 L0 70 Z" fill="#ffffff"/>
      <path d="M0 26 C150 16 300 44 430 50 C510 53 560 42 590 34 L590 70 L0 70 Z" fill="#3aae49"/>
    </svg>
    <div class="website">www.harrowfieldagri.com</div>
  </section>

</main>
</body>
</html>
```